Snapframe Party Rentals New Business Card*

Need a business card designed for a Photo Booth Hire company.Must look very professional and colorful.A new creative logo would be a bonus. Our current logo is attached on here.

Contact Information for Business Card

Business Name: SNAPFRAME PARTY RENTALS
Contact Person: MARCUS OKAFOR
Mobile: 0491862035
Email: INFO@SNAPFRAMEPARTY.EXAMPLE
Website: WWW.SNAPFRAMEPARTY.EXAMPLE
Facebook: WWW.SOCIALNET.EXAMPLE/SNAPFRAME.PARTY.RENT

Font styles to use
Serif
Sans Serif
Script

Colors

Designer to choose colors to be used in the design.

Requirements
Must have
• Bonus if the colors match our website.

```html
<!DOCTYPE html>
<html lang="en">
<head>
<meta charset="utf-8">
<title>Snapframe Party Rentals – Business Card</title>
<link href="https://fonts.googleapis.com/css2?family=Montserrat:wght@400;500;700;800&family=Marcellus&display=swap" rel="stylesheet">
<style>
  :root {
    --backdrop: #2e2e2e;
    --card-light: #e7e8ea;
    --ink: #111111;
    --ink-soft: #555555;
    --band-grey: #6b6b6d;
    --card-dark: #000000;
    --text-pale: #d2d2d2;
    --text-silver: #b9b9b9;
  }
  * { margin: 0; padding: 0; box-sizing: border-box; }
  html, body { width: 974px; height: 1200px; overflow: hidden; }
  body {
    background: var(--backdrop);
    font-family: "Montserrat", Arial, sans-serif;
    position: relative;
  }
  .card {
    position: absolute;
    border-radius: 18px;
    overflow: hidden;
  }
  .card-front {
    left: 123px; top: 131px; width: 748px; height: 436px;
    background: var(--card-light);
  }
  .card-back {
    left: 125px; top: 634px; width: 746px; height: 433px;
    background: var(--card-dark);
  }
  .wave { position: absolute; left: 0; top: 0; width: 748px; height: 436px; }
  .holder { position: absolute; left: 39px; top: 62px; }
  .holder-name {
    font-size: 25px; letter-spacing: 0.5px; color: var(--ink); font-weight: 500;
  }
  .holder-name .surname { color: var(--ink-soft); font-weight: 400; }
  .holder-role { font-size: 14px; color: var(--ink-soft); margin-top: 2px; }
  .brand-block {
    position: absolute; left: 455px; top: 64px; width: 240px; text-align: center;
  }
  .brand-dot {
    width: 70px; height: 70px; border-radius: 50%; background: var(--ink);
    margin: 0 auto 22px;
  }
  .brand-name {
    font-weight: 800; font-size: 14.5px; line-height: 16px; color: var(--ink);
  }
  .brand-url {
    font-weight: 800; font-size: 6.5px; color: var(--ink); margin-top: 2px;
  }
  .contacts {
    position: absolute; left: 42px; top: 318px; list-style: none;
  }
  .contacts li {
    display: flex; align-items: center; height: 22px;
    font-size: 15px; color: var(--text-pale);
  }
  .contacts svg { width: 13px; height: 13px; margin-right: 14px; flex: none; }
  .back-brand {
    position: absolute; left: 0; width: 100%; top: 146px; text-align: center;
    font-family: "Marcellus", Georgia, serif; color: var(--text-silver);
    font-size: 38px; line-height: 62px; letter-spacing: 1px;
  }
  .tagline {
    position: absolute; left: 0; width: 100%; top: 266px; text-align: center;
    font-weight: 800; font-size: 10px; color: var(--text-silver); letter-spacing: 0.6px;
  }
</style>
</head>
<body>
  <section class="card card-front">
    <svg class="wave" viewBox="0 0 748 436" aria-hidden="true">
      <path d="M0 257 C120 222 230 215 340 250 C430 280 500 330 600 332 C680 334 720 322 748 316 L748 436 L0 436 Z" fill="var(--band-grey)"/>
      <path d="M0 268 C130 236 240 230 345 264 C440 296 505 350 610 352 C690 353 725 340 748 334 L748 436 L0 436 Z" fill="var(--card-dark)"/>
    </svg>
    <div class="holder">
      <h1 class="holder-name">MARCUS <span class="surname">OKAFOR</span></h1>
      <p class="holder-role">Director</p>
    </div>
    <div class="brand-block">
      <div class="brand-dot"></div>
      <p class="brand-name">SNAPFRAME<br>PARTY RENTALS</p>
      <p class="brand-url">WWW.SNAPFRAMEPARTY.EXAMPLE</p>
    </div>
    <ul class="contacts">
      <li><svg viewBox="0 0 16 16"><path d="M4 1 L6.5 4.5 L5 6.5 C6 8.5 7.5 10 9.5 11 L11.5 9.5 L15 12 L13 15 C7 14 2 9 1 3 Z" fill="var(--text-pale)"/></svg>0491862035</li>
      <li><svg viewBox="0 0 16 16"><rect x="1" y="3" width="14" height="10" fill="var(--text-pale)"/><path d="M1 3 L8 9 L15 3" stroke="var(--card-dark)" stroke-width="1.3" fill="none"/></svg>info@snapframeparty.example</li>
      <li><svg viewBox="0 0 16 16"><circle cx="8" cy="8" r="6.5" fill="var(--text-pale)"/><path d="M1.5 8 H14.5 M8 1.5 C5 5 5 11 8 14.5 C11 11 11 5 8 1.5" stroke="var(--card-dark)" stroke-width="1" fill="none"/></svg>www.snapframeparty.example</li>
      <li><svg viewBox="0 0 16 16"><circle cx="8" cy="8" r="4" fill="var(--text-pale)"/></svg>www.socialnet.example/snapframe.party.rent</li>
    </ul>
  </section>

  <section class="card card-back">
    <p class="back-brand">SNAPFRAME<br>PARTY RENTALS</p>
    <p class="tagline">FRAMING EVERY CELEBRATION WITH FUN, STYLE AND SMILES</p>
  </section>
</body>
</html>
```